UK Online Auction Site needs a clever design

We need a contemporary landing page and registration page design for a UK auction website, that look equally at home on PC's and tablets . The design should be fresh, bright, clean, professional, robust, and familiar. We would like to see something clever but functional.

```html
<!DOCTYPE html>
<html lang="en">
<head>
<meta charset="utf-8">
<title>Gavelry – UK Online Auctions</title>
<link href="https://fonts.googleapis.com/css2?family=Arimo:ital,wght@0,400;0,700;1,700&family=Varela+Round&family=Dancing+Script:wght@600&display=swap" rel="stylesheet">
<style>
:root{
  --blue:#1f7fc9;
  --blue-dark:#0f6cb4;
  --blue-light:#86b9e0;
  --orange:#e8521a;
  --page:#ececec;
  --panel:#f7f7f7;
  --text:#555;
  --muted:#888;
  --dark:#1e1e1e;
  --white:#fff;
}
*{box-sizing:border-box;margin:0;padding:0}
html,body{width:1200px;height:3141px;overflow:hidden}
body{background:var(--page);font-family:"Arimo",Arial,sans-serif;color:var(--text);position:relative}
.abs{position:absolute}

/* header */
.site-header{position:absolute;left:0;top:0;width:1200px;height:118px;background:linear-gradient(#fafafa,#eaeaea)}
.brand{position:absolute;left:98px;top:34px;display:flex;align-items:center;gap:12px;font-size:44px;font-weight:700;color:var(--blue)}
.brand .dot{width:22px;height:22px;border-radius:50%;background:var(--blue)}
.top-links{position:absolute;right:100px;top:13px;font-size:12px;color:#444}
.top-links span{margin:0 8px}
.search{position:absolute;left:540px;top:58px;width:560px;height:42px;border:1px solid #ccc;border-radius:21px;background:var(--white);display:flex;align-items:center}
.search .cat{width:160px;padding-left:38px;font-size:12px;color:#444;display:flex;align-items:center;gap:14px;height:100%;border-right:1px solid #ddd}
.search svg.mag{position:absolute;right:16px;top:11px}

.main-nav{position:absolute;left:0;top:118px;width:1200px;height:50px;background:linear-gradient(var(--blue),var(--blue-dark));color:var(--white);font-size:13px}
.main-nav a{position:absolute;top:18px;color:var(--white);text-decoration:none}
.main-nav .sep{position:absolute;top:10px;width:1px;height:30px;background:rgba(255,255,255,.35)}
.cart{position:absolute;left:862px;top:15px;display:flex;align-items:center;gap:10px;font-size:12px}

/* hero */
.hero{position:absolute;left:0;top:170px;width:1200px;height:481px;background:linear-gradient(#9c9c9c,#d6d6d6 45%,#b9b9b9)}
.hero-photo{position:absolute;left:0;top:0;width:1200px;height:481px;background:radial-gradient(ellipse at 30% 40%,#e2e2e2,#9a9a9a 75%)}
.hero-product{position:absolute;left:538px;top:14px;width:316px;height:256px;border-radius:18px;background:linear-gradient(#3b3b3b,#151515)}
.hero-copy{position:absolute;left:551px;top:292px;color:#333}
.hero-copy .pre{font-family:"Varela Round",sans-serif;font-size:28px;color:#333}
.hero-copy .head{font-family:"Varela Round",sans-serif;font-size:46px;color:var(--blue);margin-top:2px;line-height:1}
.hero-copy .sub{font-family:"Varela Round",sans-serif;font-size:24px;color:var(--blue);margin-top:6px}
.hero-copy .small{font-size:15px;color:var(--white);margin-top:6px;line-height:21px}
.hero-arrow{position:absolute;top:244px;width:42px;height:42px;border-radius:50%;background:#111}

/* panels */
.panel{position:absolute;top:683px;height:266px;border-radius:8px;overflow:hidden;box-shadow:0 1px 4px rgba(0,0,0,.18)}
.welcome{left:100px;width:241px;background:linear-gradient(#dcdcdc,#f0f0f0)}
.welcome h3{font-family:"Dancing Script",cursive;font-size:22px;color:#333;margin:18px 0 0 12px;font-weight:600}
.welcome h3 span{color:var(--white)}
.welcome p{font-size:13px;line-height:19px;color:#888;margin:10px 18px 0 16px}
.panel-band{position:absolute;left:0;bottom:0;width:100%;height:55px;background:linear-gradient(var(--blue),var(--blue-dark));color:var(--white)}
.welcome .panel-band{font-size:18px;padding:17px 0 0 56px}
.signin{left:366px;width:468px;background:linear-gradient(var(--white),#e6e6e6)}
.signin h2{font-family:"Varela Round",sans-serif;font-size:27px;color:var(--blue);margin:18px 0 0 24px;font-weight:400}
.signin .lead{font-size:13px;color:#888;margin:8px 0 0 24px;line-height:19px;width:380px}
.field{position:absolute;left:24px;width:210px;height:28px;border:1px solid #ddd;background:var(--white);font-size:11px;color:#888;padding:8px 0 0 8px}
.btn-signin{position:absolute;left:254px;top:119px;width:192px;height:60px;background:linear-gradient(#2d93dc,var(--blue-dark));color:var(--white);font-size:21px;text-align:center;line-height:60px;border-radius:3px}
.signin .reg{position:absolute;left:34px;top:207px;font-size:13px;color:#777}
.signin .reg b{color:var(--blue);font-weight:400}
.bidding{left:856px;width:241px;background:linear-gradient(#e9e9e9,#f5f5f5)}
.bidding h3{font-family:"Dancing Script",cursive;font-size:24px;color:#333;margin:6px 0 0 16px;font-weight:600}
.bidding h3 span{color:var(--white)}
.bidding-photo{position:absolute;left:30px;top:36px;width:180px;height:176px;border-radius:6px;background:linear-gradient(#f4d7de,#e9a4bb 55%,#7fb0d9)}
.bidding .panel-band{font-size:11px;line-height:15px;padding:10px 10px 0 14px}

/* section titles */
.section-rule{position:absolute;left:0;width:1200px;height:1px;background:#d6d6d6}
.pill{position:absolute;height:34px;border-radius:17px;background:linear-gradient(#2d8fd6,var(--blue-dark));color:var(--white);font-size:24px;text-align:center;line-height:34px}
.plain-title{position:absolute;left:0;width:1200px;text-align:center;font-size:23px;color:var(--blue)}
.plain-title span{background:var(--page);padding:0 10px}

/* products */
.product{position:absolute;width:230px;text-align:center}
.thumb{width:172px;height:172px;margin:0 auto;border-radius:50%;border:3px solid #cfcfcf;background:var(--white);display:flex;align-items:center;justify-content:center}
.thumb .pic{width:86px;height:72px;border-radius:8px;background:linear-gradient(#cfcfcf,#6a6a6a)}
.thumb .pic.jeans{width:56px;height:110px;border-radius:4px;background:linear-gradient(#4d6f98,#1f3350)}
.product .name{font-size:12px;color:#777;margin-top:16px}
.product .price{font-size:12px;color:var(--orange);margin-top:3px}
.actions{display:flex;justify-content:center;gap:6px;margin-top:16px}
.btn{width:70px;height:35px;line-height:35px;font-size:13px;color:var(--white);border-radius:3px}
.btn.add{background:#8a8a8a}
.btn.bid{background:var(--blue-light)}
.sale{position:absolute;left:26px;top:-8px;width:38px;height:38px;border-radius:50%;background:#f08a12;color:var(--white);font-size:9px;font-weight:700;line-height:38px;text-align:center}

/* gallery */
.tile{position:absolute;border-bottom:7px solid var(--orange)}
.tile-photo{width:100%;height:100%}
.tile-add{position:absolute;left:98px;top:80px;width:38px;height:38px;background:rgba(255,255,255,.35);color:var(--white);font-size:28px;line-height:36px;text-align:center}
.tile-caption{position:absolute;left:0;bottom:0;width:100%;height:52px;background:rgba(90,90,90,.55);color:var(--white);font-size:23px;padding:12px 0 0 20px;font-family:"Varela Round",sans-serif}
.tile-caption i{position:absolute;right:16px;top:11px;width:30px;height:30px;border-radius:50%;background:var(--blue)}

/* footer */
.site-footer{position:absolute;left:0;top:2904px;width:1200px;height:183px;background:var(--blue-dark)}
.fcol{position:absolute;top:30px;color:var(--white)}
.fcol h4{font-size:13px;font-weight:700;margin-bottom:8px}
.fcol li{list-style:none;font-size:10.5px;line-height:18px}
.social{position:absolute;left:840px;top:106px;display:flex;gap:8px}
.social i{width:30px;height:30px;border-radius:4px;display:block}
.legal{position:absolute;left:0;top:3087px;width:1200px;height:54px;background:var(--dark);color:#ddd;font-size:12px}
.legal .copy{position:absolute;left:126px;top:21px}
.cards{position:absolute;right:112px;top:17px;display:flex;gap:6px}
.cards i{width:44px;height:22px;border-radius:3px;background:#e6e6e6;display:block}
</style>
</head>
<body>

<header class="site-header">
  <div class="brand"><span class="dot"></span>Gavelry</div>
  <nav class="top-links">Login<span>|</span>Register<span>|</span>Home<span>|</span>Contact us</nav>
  <div class="search">
    <div class="cat">All Categories
      <svg width="12" height="8" viewBox="0 0 12 8"><path d="M0 0h12L6 8z" fill="#1f7fc9"/></svg>
    </div>
    <svg class="mag" width="20" height="20" viewBox="0 0 20 20"><circle cx="8" cy="8" r="6" fill="none" stroke="#0f6cb4" stroke-width="2.5"/><path d="M12.5 12.5l6 6" stroke="#0f6cb4" stroke-width="3"/></svg>
  </div>
</header>

<nav class="main-nav">
  <a style="left:143px">HOME</a><span class="sep" style="left:222px"></span>
  <a style="left:244px">RETURNS</a><span class="sep" style="left:344px"></span>
  <a style="left:368px">SHIPPING</a><span class="sep" style="left:466px"></span>
  <a style="left:490px">FEEDBACK</a><span class="sep" style="left:597px"></span>
  <a style="left:622px">CONTACT US</a>
  <div class="cart">
    <svg width="28" height="22" viewBox="0 0 28 22"><path d="M1 2h5l3 12h14l3-9H8" fill="none" stroke="#f5a623" stroke-width="2.5"/><circle cx="11" cy="19" r="2" fill="#f5a623"/><circle cx="21" cy="19" r="2" fill="#f5a623"/></svg>
    <span>My cart:</span><span style="margin-left:16px">1 item(s)&nbsp; | &nbsp;$ 270 (USD)</span>
  </div>
</nav>

<section class="hero">
  <div class="hero-photo" role="img" aria-label="Black and white photo of a woman leaping against a cloudy sky"></div>
  <div class="hero-product" role="img" aria-label="Product photo of a digital SLR camera with a request-a-quote ribbon"></div>
  <div class="hero-copy">
    <div class="pre">Don’t Worry</div>
    <div class="head">Come To Gavelry</div>
    <div class="sub">Check Our Our New Items</div>
    <div class="small">Beautiful &amp; Elegant Inside a minimalistic portfolio concept.<br>Wondrous is a real High definition designed.</div>
  </div>
  <div class="hero-arrow" style="left:31px"><svg width="42" height="42" viewBox="0 0 42 42"><path d="M24 14l-8 7 8 7" fill="none" stroke="#fff" stroke-width="3"/></svg></div>
  <div class="hero-arrow" style="left:1113px"><svg width="42" height="42" viewBox="0 0 42 42"><path d="M18 14l8 7-8 7" fill="none" stroke="#fff" stroke-width="3"/></svg></div>
</section>

<aside class="panel welcome">
  <h3><span>Welcome</span> to Gavelry</h3>
  <p>Lorem ipsum dolor sit amet, consectetur adipiscing elit. Sed vitae posuere metus. Pellentesque sagittis mi amet est pretium pharetra. Curabitur hendrerit bibendum augue ultrices tempus.</p>
  <div class="panel-band">Read More</div>
</aside>

<section class="panel signin">
  <h2>Sign In here</h2>
  <p class="lead">Sign-in to your account in order to buy, sell or manage your preferences.</p>
  <div class="field" style="top:120px">Your Name</div>
  <div class="field" style="top:152px">Your Email</div>
  <div class="btn-signin">SIGN IN</div>
  <div class="reg">Don’t have an account? <b>Register ›</b></div>
</section>

<aside class="panel bidding">
  <h3><span>Online</span> Bidding</h3>
  <div class="bidding-photo" role="img" aria-label="Photo of a smiling shopper holding colourful shopping bags"></div>
  <div class="panel-band">Valuable branded picnic sets draw attention with a custom...</div>
</aside>

<!-- New Items -->
<div class="section-rule" style="top:1034px"></div>
<div class="pill" style="left:429px;top:1018px;width:304px">New Items</div>
<div class="product" style="left:71px;top:1082px"><div class="thumb"><div class="pic" role="img" aria-label="Compact camera"></div></div><div class="name">Promotional Picnic Sets</div><div class="price">$ 125.000</div><div class="actions"><div class="btn add">Add</div><div class="btn bid">Bid</div></div></div>
<div class="product" style="left:358px;top:1082px"><div class="thumb"><div class="pic" role="img" aria-label="Compact camera"></div></div><div class="name">Promotional Picnic Sets</div><div class="price">$ 125.000</div><div class="actions"><div class="btn add">Add</div><div class="btn bid">Bid</div></div></div>
<div class="product" style="left:618px;top:1082px"><div class="thumb"><div class="pic" role="img" aria-label="Compact camera"></div></div><div class="name">Promotional Picnic Sets</div><div class="price">$ 125.000</div><div class="actions"><div class="btn add">Add</div><div class="btn bid">Bid</div></div></div>
<div class="product" style="left:886px;top:1082px"><div class="thumb"><div class="pic" role="img" aria-label="Compact camera"></div></div><div class="name">Promotional Picnic Sets</div><div class="price">$ 125.000</div><div class="actions"><div class="btn add">Add</div><div class="btn bid">Bid</div></div></div>

<!-- Best Selling -->
<div class="section-rule" style="top:1471px"></div>
<div class="plain-title" style="top:1457px"><span>Best Selling Items</span></div>
<div class="product" style="left:71px;top:1524px"><div class="thumb"><div class="pic" role="img" aria-label="Compact camera"></div></div><div class="name">Promotional Picnic Sets</div><div class="price">$ 125.000</div><div class="actions"><div class="btn add">Add</div><div class="btn bid">Bid</div></div></div>
<div class="product" style="left:361px;top:1524px"><div class="thumb"><div class="pic" role="img" aria-label="Compact camera"></div></div><div class="name">Promotional Picnic Sets</div><div class="price">$ 125.000</div><div class="actions"><div class="btn add">Add</div><div class="btn bid">Bid</div></div></div>
<div class="product" style="left:629px;top:1524px"><div class="thumb"><div class="pic" role="img" aria-label="Compact camera"></div></div><div class="name">Promotional Picnic Sets</div><div class="price">$ 125.000</div><div class="actions"><div class="btn add">Add</div><div class="btn bid">Bid</div></div></div>
<div class="product" style="left:897px;top:1524px"><div class="thumb"><div class="pic" role="img" aria-label="Compact camera"></div></div><div class="name">Promotional Picnic Sets</div><div class="price">$ 125.000</div><div class="actions"><div class="btn add">Add</div><div class="btn bid">Bid</div></div></div>

<!-- Ending Soon -->
<div class="section-rule" style="top:1893px"></div>
<div class="pill" style="left:418px;top:1876px;width:306px">Ending Soon Items</div>
<div class="product" style="left:71px;top:1951px"><span class="sale">SALE</span><div class="thumb"><div class="pic jeans" role="img" aria-label="Pair of blue jeans"></div></div><div class="name">Promotional Picnic Sets</div><div class="price">$ 125.000</div><div class="actions"><div class="btn add">Add</div><div class="btn bid">Bid</div></div></div>
<div class="product" style="left:350px;top:1951px"><div class="thumb"><div class="pic jeans" role="img" aria-label="Pair of blue jeans"></div></div><div class="name">Promotional Picnic Sets</div><div class="price">$ 125.000</div><div class="actions"><div class="btn add">Add</div><div class="btn bid">Bid</div></div></div>
<div class="product" style="left:636px;top:1951px"><div class="thumb"><div class="pic jeans" role="img" aria-label="Pair of blue jeans"></div></div><div class="name">Promotional Picnic Sets</div><div class="price">$ 125.000</div><div class="actions"><div class="btn add">Add</div><div class="btn bid">Bid</div></div></div>
<div class="product" style="left:896px;top:1951px"><div class="thumb"><div class="pic jeans" role="img" aria-label="Pair of blue jeans"></div></div><div class="name">Promotional Picnic Sets</div><div class="price">$ 125.000</div><div class="actions"><div class="btn add">Add</div><div class="btn bid">Bid</div></div></div>

<!-- Best Look -->
<div class="section-rule" style="top:2318px"></div>
<div class="pill" style="left:410px;top:2301px;width:306px">Best Look Items</div>
<div class="tile" style="left:113px;top:2385px;width:475px;height:473px"><div class="tile-photo" role="img" aria-label="Fashion photo of a woman in sunglasses carrying a tote bag" style="background:linear-gradient(135deg,#7a1d3a,#b9425a 50%,#e8a27f)"></div></div>
<div class="tile" style="left:599px;top:2385px;width:232px;height:230px"><div class="tile-photo" role="img" aria-label="Photo of a patterned shoulder bag beside denim shorts" style="background:linear-gradient(#4a6fa0,#b68d73)"></div></div>
<div class="tile" style="left:840px;top:2385px;width:232px;height:230px"><div class="tile-photo" role="img" aria-label="Photo of a handbag with a blue overlay" style="background:linear-gradient(#3f86c7,#2c6aa8)"></div><div class="tile-add">+</div></div>
<div class="tile" style="left:599px;top:2628px;width:473px;height:230px"><div class="tile-photo" role="img" aria-label="Photo of bracelets and a watch on crossed arms with a clutch bag" style="background:linear-gradient(90deg,#8b5e4a,#d8b6a2 50%,#9aa9c0)"></div><div class="tile-caption">Nicely Neutral<i></i></div></div>

<footer class="site-footer">
  <div class="fcol" style="left:126px"><h4>Home</h4><ul><li>About Us</li><li>Sitemap</li><li>Website Terms</li><li>Terms of Business</li><li>Privacy Policy</li></ul></div>
  <div class="fcol" style="left:283px"><h4>IT Solutions</h4><ul><li>Business Websites</li><li>Reviews</li><li>Quick Tour</li><li>Pricing</li><li>Free Trial</li></ul></div>
  <div class="fcol" style="left:461px"><h4>Web Develoment</h4><ul><li>Marketing Tips</li><li>Search Optimisation</li><li>Social Media</li><li>Video Marketing</li><li>Business Cases</li></ul></div>
  <div class="fcol" style="left:664px"><h4>Web Marketing</h4><ul><li>Help/Contact us</li><li>Business directory</li><li>Legal notices</li><li>Privacy policy</li><li>Terms &amp; Conditions</li></ul></div>
  <div class="fcol" style="left:840px"><h4>About Us</h4><ul><li>Blog</li><li>Contact us</li></ul></div>
  <div class="social"><i style="background:#3b5b98"></i><i style="background:#39a9e0"></i><i style="background:#c4302b"></i><i style="background:#f28a1e"></i></div>
</footer>

<div class="legal">
  <div class="copy">© 2014 UK based auction website &nbsp;|&nbsp; Login</div>
  <div class="cards"><i></i><i></i><i></i><i></i><i></i><i></i></div>
</div>

</body>
</html>
```